Improvements to a dating website design

Current site: http://vorlimo.example:8079/pages/index.html

I am looking for an update to our current design that will be more engaging to our users. The current version feels a little too brash and business-like. I would like to make it feel more inviting, to women especially, but men as well. The site is aimed at Indians and other South Asians in their mid 20s to late 30s, living primarily in the U.S. and Canada. It is still under development and not yet live.

This redesign is for the public part of the site, and not the inside pages for member users. To be clear, the sections to be redesigned are:
- the home landing page
- How It Works
- FAQ
- About Us
- Sign Up

Please take the text from the site for the copy.

Thanks, and looking forward to seeing your designs!
Updates

Project Deadline Extended Reason: I would like to give people a little time to develop good ideas. Added Friday, August 21, 2015

Target Market(s)

Our users will be:
- South Asian (indian, Pakistani, Sri Lankan, etc.) single men and women
- in their mid 20s to late 30s
- living primarily in the U.S. and Canada

Industry/Entity Type

Dating

Coding

Coded - Design and coding required

Number of Pages Required

1 page

Requirements
Must have
• I am updating the requirements for this to be a coded HTML/CSS page. (I've also increased the budget, added a 2nd place prize, extended the deadline, and guaranteed payment.) The design should be suitable for "responsiveness" to different browser window sizes, down to mobile phones.
• The main image, which is attached in the files, should continue to be the main image. However, the image can be re-cropped and re-filtered to better match the design. I am happy with the image being used as a full-page backdrop on the home page area, but I'm open to changes.
• All of the text on the current site should be part of the updated design. However, it can be reformatted and laid out differently. (Headings and navigation can be different.)
• The 'What's a Tandem Evening?' section should have the sentences broken out from the single paragraph so that it is easier to read. Each sentence can be a distinct item.
Nice to have
• This site is about online events (called 'Tandem Evenings') where users can meet and get to know each other. So please keep in mind that the point of the website is to
• - educate users how Tandem Evenings work
• - get them to purchase a reservation for the next Tandem Evening (which will be the first).
• Also, the design does not have to be completely different from the existing design, as the site is not yet live and has not been seen by users. Incremental, even small, changes to the current site that result in a captivating design would be just fine.
• Please consider using colors other than the logo colors.
Should not have
• It is not easy to find the right photo, so if you put additional images of people in your design, please make sure they
• - look South Asian (Indian, Pakistani, Sri Lankan, etc.)
• - are wearing western clothing in a western setting
• Also, any images must be available for rights-free licensing. I can't accept submissions that don't follow these guidelines.
• This site is not like other dating sites, in that it has no profiles for users to go through and see. So please don't include any samples of these. Also, no testimonials, as this is a new site.
• There should not be any hearts in the design!
• Any iconified version of the word 'Vorlimo' must be either the actual full-color logo, or a monochrome version of it. Please don't use other word shapes for the site name.

```html
<!DOCTYPE html>
<html lang="en">
<head>
<meta charset="utf-8">
<title>Vorlimo – Home</title>
<link rel="stylesheet" href="https://fonts.googleapis.com/css2?family=Open+Sans:wght@400;600;700;800&display=swap">
<style>
:root{
  --magenta:#b0136a;
  --green:#7aa531;
  --ink:#3a3a3a;
  --muted:#7b7b7b;
  --line:#e3e3e3;
  --ring:#e35a6c;
  --dark-box:#3d3d3d;
  --gold:#f2c230;
  --blue:#2d78b8;
  --footer:#1f5c9c;
  --white:#ffffff;
}
*{box-sizing:border-box;margin:0;padding:0}
html,body{width:1200px;height:2424px;overflow:hidden}
body{font-family:"Open Sans",Arial,sans-serif;color:var(--ink);background:var(--white)}
.wrap{width:1100px;margin:0 auto;position:relative}

/* header */
.site-header{height:52px;border-bottom:1px solid var(--line);background:var(--white)}
.site-header .wrap{display:flex;align-items:center;height:52px}
.brand{display:flex;align-items:center;gap:8px;font-weight:700;font-size:28px;color:var(--magenta);letter-spacing:-.5px}
.brand-dot{width:10px;height:10px;background:var(--magenta);border-radius:50%}
.main-nav{margin-left:auto;display:flex;gap:34px;font-size:12px;font-weight:700;letter-spacing:.4px}
.main-nav a{color:var(--ink);text-decoration:none}
.main-nav a.active{color:var(--magenta)}
.social{display:flex;gap:6px;margin-left:40px}
.social span{width:26px;height:26px;border:1px solid var(--line);display:block;position:relative}
.social span::after{content:"";position:absolute;inset:8px;background:var(--magenta)}

/* hero */
.hero{height:500px;position:relative;background:linear-gradient(100deg,#3b2a22 0%,#6b5446 35%,#8a7666 60%,#4a3d35 100%)}
.hero-copy{position:absolute;left:80px;top:110px;color:var(--white)}
.hero-copy h1{font-size:88px;font-weight:800;line-height:1;letter-spacing:2px}
.hero-copy h2{font-size:40px;font-weight:400;letter-spacing:3px;line-height:1.2}
.hero-copy p{font-size:13px;width:300px;margin-top:8px;line-height:1.5}
.slide-arrow{position:absolute;top:225px;width:34px;height:34px;background:rgba(255,255,255,.35);display:flex;align-items:center;justify-content:center}
.slide-arrow.prev{left:18px}.slide-arrow.next{right:18px}
.login-bar{position:absolute;left:0;right:0;bottom:32px;height:50px;background:var(--white);display:flex;align-items:center;justify-content:center;gap:14px}
.field{width:230px;height:30px;border:1px solid #d4d4d4;display:flex;align-items:center;gap:8px;padding-left:8px;font-size:11px;color:var(--muted)}
.field svg{flex:none}
.btn{display:inline-block;background:var(--magenta);color:var(--white);font-size:12px;font-weight:700;letter-spacing:.5px;padding:9px 20px;text-decoration:none;text-transform:uppercase}

/* section headings */
.section-title{font-size:34px;font-weight:800;color:var(--green);letter-spacing:.5px}
.section-rule{height:2px;background:var(--green);width:100%;margin:12px 0 22px}
.body-text{font-size:13px;line-height:1.75;color:var(--muted)}

.about{height:408px;padding-top:48px}
.about .btn{margin-top:26px}

.event{height:340px;padding-top:30px}
.event-row{display:flex;gap:40px;align-items:flex-start}
.event-row .body-text{width:560px}
.event-box{width:500px;height:160px;background:var(--dark-box);display:flex;flex-direction:column;align-items:center;justify-content:center;gap:18px;text-align:center;padding:0 30px}
.event-box p{color:var(--gold);font-size:24px;font-weight:700;line-height:1.3}
.btn.blue{background:var(--blue)}

.how{height:590px;padding-top:44px}
.steps{position:relative;display:flex;justify-content:space-between;margin-top:34px}
.step{width:200px;text-align:center}
.step-icon{width:110px;height:110px;border:4px solid var(--ring);border-radius:50%;margin:0 auto;display:flex;align-items:center;justify-content:center;background:var(--white);position:relative;z-index:1}
.step h3{font-size:14px;font-weight:700;margin:18px 0 10px;letter-spacing:.5px}
.step p{font-size:12px;line-height:1.6;color:var(--muted)}
.step-arrows{position:absolute;left:0;top:0;z-index:0}
.how-actions{display:flex;justify-content:center;gap:70px;margin-top:38px}

.faq{height:480px;padding-top:12px}
.faq-grid{display:grid;grid-template-columns:1fr 1fr;column-gap:60px;row-gap:24px}
.faq-item{display:flex;gap:16px}
.q-mark{flex:none;width:34px;height:34px;border-radius:50%;background:var(--green);color:var(--white);font-weight:800;font-size:18px;display:flex;align-items:center;justify-content:center}
.faq-item h4{font-size:15px;font-weight:600;color:var(--ink);margin-bottom:6px;line-height:1.35}
.faq-item p{font-size:11.5px;line-height:1.6;color:var(--muted)}
.faq-actions{text-align:center;margin-top:28px}

.site-footer{height:54px;background:var(--footer);color:#dce7f3;font-size:11px;display:flex;align-items:center;justify-content:center}
</style>
</head>
<body>

<header class="site-header">
  <div class="wrap">
    <div class="brand"><span class="brand-dot"></span>vorlimo</div>
    <nav class="main-nav">
      <a class="active" href="#">HOME</a>
      <a href="#">HOW IT WORKS</a>
      <a href="#">FAQ</a>
      <a href="#">ABOUT US</a>
    </nav>
    <div class="social"><span></span><span></span><span></span></div>
  </div>
</header>

<section class="hero" role="img" aria-label="Photograph of a smiling young couple standing close together outdoors">
  <div class="hero-copy">
    <h1>LOVE</h1>
    <h2>CHEMISTRY</h2>
    <p>Find the one you truly connect with, starting from a single conversation.</p>
  </div>
  <div class="slide-arrow prev"><svg width="12" height="16" viewBox="0 0 12 16"><path d="M9 2L3 8l6 6" fill="none" stroke="#fff" stroke-width="2.5"/></svg></div>
  <div class="slide-arrow next"><svg width="12" height="16" viewBox="0 0 12 16"><path d="M3 2l6 6-6 6" fill="none" stroke="#fff" stroke-width="2.5"/></svg></div>
  <form class="login-bar">
    <label class="field"><svg width="14" height="14" viewBox="0 0 14 14"><circle cx="7" cy="4.5" r="3" fill="#b0136a"/><path d="M1 14c0-4 3-5.5 6-5.5s6 1.5 6 5.5z" fill="#b0136a"/></svg>user id</label>
    <label class="field"><svg width="14" height="14" viewBox="0 0 14 14"><rect x="2" y="6" width="10" height="8" fill="#b0136a"/><path d="M4 6V4a3 3 0 0 1 6 0v2" fill="none" stroke="#b0136a" stroke-width="1.6"/></svg>password</label>
    <a class="btn" href="#">Login</a>
    <a class="btn" href="#">Register Now</a>
  </form>
</section>

<main>
<section class="about">
  <div class="wrap">
    <h2 class="section-title">ABOUT US</h2>
    <div class="section-rule"></div>
    <p class="body-text">We started Vorlimo because meeting someone who shares your background and your values should not feel like a chore. Our community brings together single South Asian men and women across the U.S. and Canada who want something real. Instead of endless browsing, we host friendly online evenings where members can talk, laugh and discover genuine chemistry in a relaxed setting. Every detail is designed to keep things comfortable, respectful and fun, so you can focus on the person in front of you. We believe great relationships begin with honest conversation, and we are here to help those first conversations happen naturally, at a pace that feels right for you and the people you meet along the way.</p>
    <a class="btn" href="#">View More</a>
  </div>
</section>

<section class="event">
  <div class="wrap">
    <h2 class="section-title">TANDEM EVENING</h2>
    <div class="section-rule"></div>
    <div class="event-row">
      <p class="body-text">It is a fully hosted online evening for singles. You join from home, answer a few light questions and are matched with people who share your interests. Each short chat lets you get to know someone new, and when the evening ends you decide who you would like to see again. It is simple, warm and a great way to start.</p>
      <div class="event-box">
        <p>On June 1, join us for the first ever Vorlimo Tandem Evening.</p>
        <a class="btn blue" href="#">Sign Up Here</a>
      </div>
    </div>
  </div>
</section>

<section class="how">
  <div class="wrap">
    <h2 class="section-title">HOW IT WORKS</h2>
    <div class="section-rule"></div>
    <div class="steps">
      <svg class="step-arrows" width="1100" height="120" viewBox="0 0 1100 120" aria-hidden="true">
        <g fill="none" stroke="#e35a6c" stroke-width="2">
          <path d="M170 60 Q220 20 275 60"/><path d="M267 54l8 6-10 2"/>
          <path d="M395 60 Q445 20 500 60"/><path d="M492 54l8 6-10 2"/>
          <path d="M620 60 Q670 100 725 60"/><path d="M715 62l10-2-4 9"/>
          <path d="M845 60 Q895 20 950 60"/><path d="M942 54l8 6-10 2"/>
        </g>
      </svg>
      <div class="step">
        <div class="step-icon"><svg width="46" height="46" viewBox="0 0 46 46" fill="none" stroke="#e35a6c" stroke-width="3"><path d="M20 8h16v30H20"/><path d="M6 23h20M19 16l7 7-7 7"/></svg></div>
        <h3>LOG IN</h3>
        <p>Create your account, answer a short questionnaire and reserve your seat for the next evening.</p>
      </div>
      <div class="step">
        <div class="step-icon"><svg width="46" height="46" viewBox="0 0 46 46" fill="none" stroke="#e35a6c" stroke-width="3"><circle cx="23" cy="23" r="17"/><path d="M23 12v11l8 5"/></svg></div>
        <h3>TIME OF EVENT</h3>
        <p>On the night, sign in a few minutes early and our host will welcome everyone and explain the steps.</p>
      </div>
      <div class="step">
        <div class="step-icon"><svg width="46" height="46" viewBox="0 0 46 46" fill="none" stroke="#e35a6c" stroke-width="3"><rect x="6" y="10" width="34" height="26"/><circle cx="16" cy="19" r="3"/><path d="M6 32l11-9 8 6 6-5 9 8"/></svg></div>
        <h3>PHOTOS</h3>
        <p>Share a photo with each match, then decide together whether you would like to keep chatting.</p>
      </div>
      <div class="step">
        <div class="step-icon"><svg width="46" height="46" viewBox="0 0 46 46" fill="none" stroke="#e35a6c" stroke-width="3"><rect x="5" y="13" width="26" height="20"/><path d="M31 20l10-6v18l-10-6"/></svg></div>
        <h3>VIDEO CHAT</h3>
        <p>Meet face to face in a short video chat, with easy prompts to keep the conversation flowing.</p>
      </div>
      <div class="step">
        <div class="step-icon"><svg width="46" height="46" viewBox="0 0 46 46" fill="none" stroke="#e35a6c" stroke-width="3"><circle cx="17" cy="23" r="10"/><circle cx="29" cy="23" r="10"/></svg></div>
        <h3>DATING</h3>
        <p>Afterwards, tell us who you liked. When it is mutual, we share contact details so you can meet.</p>
      </div>
    </div>
    <div class="how-actions">
      <a class="btn" href="#">Sign In Here</a>
      <a class="btn" href="#">Sign Up Here</a>
    </div>
  </div>
</section>

<section class="faq">
  <div class="wrap">
    <h2 class="section-title">FREQUENTLY ASKED QUESTIONS</h2>
    <div class="section-rule"></div>
    <div class="faq-grid">
      <div class="faq-item"><span class="q-mark">Q</span><div><h4>Where does the event take place?</h4><p>Everything happens online. You can join from your home on a laptop or desktop computer with a camera, so there is no need to travel anywhere at all.</p></div></div>
      <div class="faq-item"><span class="q-mark">Q</span><div><h4>What are the technology requirements to be able to take part in the event?</h4><p>You need a recent web browser, a working webcam and microphone, and a steady internet connection for the length of the evening.</p></div></div>
      <div class="faq-item"><span class="q-mark">Q</span><div><h4>Is it possible to test my system to see if it will work in the event?</h4><p>Yes. Once you sign in, a quick test page checks your camera, sound and connection, and shows you how to fix anything that is not ready.</p></div></div>
      <div class="faq-item"><span class="q-mark">Q</span><div><h4>What will other users see about me?</h4><p>Only your first name, your photo and a few answers you choose to share. Your contact details stay private unless you both agree to connect.</p></div></div>
      <div class="faq-item"><span class="q-mark">Q</span><div><h4>How long does the profile questionnaire take?</h4><p>Most members finish it in about ten minutes. The questions are light and help us match you with people you are likely to enjoy talking to.</p></div></div>
      <div class="faq-item"><span class="q-mark">Q</span><div><h4>Will you match me with people close by?</h4><p>We look at location along with your preferences, so most of your matches live in your region and meeting in person later is easy.</p></div></div>
    </div>
    <div class="faq-actions"><a class="btn" href="#">Get More FAQ's</a></div>
  </div>
</section>
</main>

<footer class="site-footer">© Vorlimo. All Rights Reserved</footer>

</body>
</html>
```